Real Estate For Sale Signage

I'm an independent agent in Lismore NSW Australia with high standards and looking for a catching 'For Sale'sign board.
I like classy, elegant, stylish and simple best.
My colours are red, white and black.
I don't have a logo or other font designs I need to stick to. I like the concept of a house or real estate design.
Before I created this project I played around on publisher and created the PDF attached. I'm not sold on it, but I don't mind the way the name has been layed out. Originally I had a white background with black & red font.
Fancy fonts for my name would be nice, but must not be busy.
Updates

Just wanted to advise that I have updated my brief and used the tools available to help get my ideas through.

Thank you for your work and time.

Kind regards
Delphine

Industry/Entity Type

Real Estate

Requirements
Must have
• For Sale
Delphine Marsk Real Estate (must stand out)
0491 572 306 (must stand out)
17 Tindale Crescent Northgrove
www.delphinemarskrealestate.example.au

```html
<!DOCTYPE html>
<html lang="en">
<head>
<meta charset="utf-8">
<title>For Sale – Delphine Marsk Real Estate</title>
<link rel="stylesheet" href="https://fonts.googleapis.com/css2?family=Open+Sans:ital,wght@0,700;1,800&family=Pinyon+Script&family=Almendra:wght@700&family=Marcellus&family=UnifrakturCook:wght@700&display=swap">
<style>
  :root {
    --black: #060304;
    --white: #ffffff;
    --red: #a80d12;
    --red-deep: #6e0a0d;
    --red-band: #b0181c;
    --gold: #d9b46a;
    --floral: #3a0a0c;
  }
  html, body {
    margin: 0;
    padding: 0;
    width: 1200px;
    height: 849px;
    overflow: hidden;
    background: var(--white);
  }
  .sign {
    position: relative;
    width: 1200px;
    height: 849px;
  }
  .sign__border {
    position: absolute;
    inset: 0;
    background: linear-gradient(135deg, var(--red) 0%, #8a3a2a 30%, var(--gold) 50%, #8a3a2a 70%, var(--red) 100%);
  }
  .sign__panel {
    position: absolute;
    left: 32px;
    top: 32px;
    width: 1136px;
    height: 785px;
    background: var(--black);
    overflow: hidden;
  }
  .sign__floral {
    position: absolute;
    inset: 0;
    background:
      radial-gradient(ellipse at 12% 30%, var(--floral) 0%, transparent 40%),
      radial-gradient(ellipse at 88% 25%, var(--floral) 0%, transparent 42%),
      radial-gradient(ellipse at 85% 75%, var(--floral) 0%, transparent 35%),
      radial-gradient(ellipse at 20% 70%, #220607 0%, transparent 35%);
  }
  .sign__headline {
    position: absolute;
    top: 2px;
    left: 0;
    width: 100%;
    margin: 0;
    text-align: center;
    font-family: "Open Sans", sans-serif;
    font-weight: 700;
    font-size: 128px;
    line-height: 1.1;
    color: var(--white);
    letter-spacing: -1px;
  }
  .sign__with {
    position: absolute;
    top: 150px;
    left: 0;
    width: 100%;
    text-align: center;
    font-family: "Pinyon Script", cursive;
    font-size: 46px;
    line-height: 1;
    color: var(--white);
  }
  .agent-name,
  .agent-trade {
    position: absolute;
    margin: 0;
    white-space: nowrap;
    font-family: "Almendra", serif;
    font-weight: 700;
    line-height: 1;
    color: var(--white);
  }
  .agent-name {
    left: 0;
    width: 100%;
    top: 225px;
    text-align: center;
    font-size: 120px;
  }
  .agent-trade {
    right: 110px;
    top: 365px;
    font-size: 90px;
  }
  .contact-phone__label {
    position: absolute;
    left: 30px;
    top: 588px;
    font-family: "UnifrakturCook", serif;
    font-weight: 700;
    font-size: 28px;
    line-height: 1;
    color: var(--white);
  }
  .contact-phone__number {
    position: absolute;
    left: 134px;
    top: 490px;
    font-family: "Open Sans", sans-serif;
    font-style: italic;
    font-weight: 800;
    font-size: 142px;
    line-height: 1;
    letter-spacing: -2px;
    color: var(--white);
    white-space: nowrap;
  }
  .info-band {
    position: absolute;
    left: 0;
    top: 634px;
    width: 100%;
    height: 151px;
    border-top: 6px solid var(--red);
    background: var(--red-band);
  }
  .info-band__photo {
    position: absolute;
    top: 0;
    height: 100%;
    width: 215px;
    background: linear-gradient(180deg, #5a1010 0%, #3b0a0a 100%);
  }
  .info-band__photo--left { left: 0; }
  .info-band__photo--right { right: 0; }
  .info-band__web,
  .info-band__address {
    position: absolute;
    left: 0;
    width: 100%;
    text-align: center;
    font-family: "Marcellus", serif;
    line-height: 1;
    color: var(--white);
    white-space: nowrap;
  }
  .info-band__web {
    top: 14px;
    font-size: 50px;
  }
  .info-band__address {
    top: 82px;
    font-size: 46px;
  }
</style>
</head>
<body>
  <main class="sign">
    <div class="sign__border" role="img" aria-label="Harlequin diamond border in red, gold and black"></div>
    <div class="sign__panel">
      <div class="sign__floral" role="img" aria-label="Dark red flourish pattern in the background"></div>

      <h1 class="sign__headline">For Sale</h1>
      <div class="sign__with">with</div>

      <h2 class="agent-name">Delphine Marsk</h2>
      <p class="agent-trade">Real Estate</p>

      <span class="contact-phone__label">phone</span>
      <span class="contact-phone__number">0491-572-306</span>

      <div class="info-band">
        <div class="info-band__photo info-band__photo--left" role="img" aria-label="Faded photo of a house"></div>
        <div class="info-band__photo info-band__photo--right" role="img" aria-label="Faded photo of a colonial style home"></div>
        <div class="info-band__web">www.delphinemarskrealestate.example.au</div>
        <div class="info-band__address">17 Tindale Crescent, Northgrove</div>
      </div>
    </div>
  </main>
</body>
</html>
```